PREMIUM AGENCY High End Business Card - A+++ Designers Wanted

** DO NOT ATTEMPT TO CONTACT ME THROUGH SEARCHING ON ZINTREL OR EMAILING ME THROUGH MY WEBSITE **

I need a fresh, contemporary business card designed using the logo attached (BRONSALK)

I have attached the font for BRONSALK

It must have a premium look and feel. The business card size must be STANDARD size.

You can submit either/both VERTICAL or HORIZONTAL designs.

FRONT: It must have the following sample information on

Paul Ardley
Director Operations
Mobile +61 452 118 906
Email paulardley@bronsalk.com
www.bronsalk.com

The REAR of the business card must have the words

CREATE INSPIRE TOMORROW

as part of the design, in the same font (NEXA) attached.

The words do not need to be in capitals, or on the same line, please design this as you see it best working.

ADDITIONAL INFORMATION
======================

The BRONSALK logo must be on the front of the card

I want Ultraviolet printing on the final design, to enhance either the NAME of the person OR the BRONSALK logo OR the words on the back of the card.

Target Market(s)

Agency, Advertising Agency, Creative, Designers

Industry/Entity Type

Media

Contact Information for Business Card

Design Agency, Contemporary, Premium look and feel, High Quality

Font styles to use
Serif
Sans Serif
Other font styles liked:
• ATTACHED TO PROJECT

Requirements
Must have
• BLACK & WHITE as the primary design, and if you feel there can be a highlighted colour, then this can be used.
• The Logo ICON attached is blue, this colour must not be changed.
• I have attached the partner brand BRONSALK MEDIA incase you need to manipulate the original files.
• ** DO NOT ATTEMPT TO CONTACT ME THROUGH SEARCHING ON ZINTREL OR EMAILING ME THROUGH MY WEBSITE **
Nice to have
• Must be Premium. I have attached some sample designs, that I like that would be a good inspiration for where this can be taken.
• My favourite design is is the KESTRAVUE2-BUSINESSCARD-TEMPLATE
Should not have
• No funny or silly standard / off the shelf designs

```html
<!DOCTYPE html>
<html lang="en">
<head>
<meta charset="utf-8">
<title>Bronsalk Business Card</title>
<link rel="stylesheet" href="https://fonts.googleapis.com/css2?family=Red+Hat+Display:wght@500;600;700&family=Open+Sans:wght@400;600&display=swap">
<style>
  :root {
    --stage: #393939;
    --paper: #ffffff;
    --ink: #111111;
    --brand-blue: #27a9e1;
    --uv-blue: #5ac6f0;
    --card-black: #050505;
    --on-blue: #ffffff;
  }
  * { box-sizing: border-box; margin: 0; padding: 0; }
  html, body {
    width: 1200px; height: 900px; overflow: hidden;
    background: var(--stage);
  }
  .card {
    position: absolute;
    top: 306px;
    width: 439px; height: 271px;
    border-radius: 12px;
    overflow: hidden;
    box-shadow: 0 3px 6px rgba(0,0,0,0.35);
  }
  /* Front */
  .card-front { left: 149px; background: var(--paper); }
  .brand {
    position: absolute; top: 0; left: 0; right: 0; height: 139px;
    display: flex; align-items: center; justify-content: center; gap: 14px;
  }
  .brand-dot {
    width: 22px; height: 22px; border-radius: 50%;
    background: var(--brand-blue);
  }
  .brand-name {
    font-family: "Red Hat Display", sans-serif;
    font-weight: 600;
    font-size: 43px;
    letter-spacing: 3.5px;
    color: var(--ink);
    line-height: 1;
  }
  .info-band {
    position: absolute; left: 0; right: 0; bottom: 0; height: 132px;
    background: var(--brand-blue);
    color: var(--on-blue);
  }
  .person { position: absolute; left: 31px; top: 36px; }
  .person-name {
    font-family: "Red Hat Display", sans-serif;
    font-weight: 700; font-size: 15.5px; line-height: 18px;
  }
  .person-role {
    font-family: "Open Sans", sans-serif;
    font-size: 11.5px; line-height: 16px;
  }
  .contacts {
    position: absolute; right: 31px; top: 38px;
    list-style: none;
    font-family: "Open Sans", sans-serif;
    font-size: 11.5px; line-height: 17px;
    text-align: right;
  }
  .contacts li { display: flex; align-items: center; justify-content: flex-end; gap: 4px; }
  .contacts svg { width: 9px; height: 9px; fill: var(--on-blue); flex: none; }

  /* Back */
  .card-back { left: 608px; background: var(--card-black); }
  .type-texture {
    position: absolute; inset: 0;
    background: linear-gradient(135deg, #121212 0%, #070707 45%, #141414 100%);
  }
  .motto {
    position: absolute; inset: 0;
    display: flex; flex-direction: column; align-items: center; justify-content: center;
    font-family: "Red Hat Display", sans-serif;
    font-weight: 500;
    font-size: 45px; line-height: 54px;
    color: var(--uv-blue);
    text-align: center;
    letter-spacing: 0.5px;
  }
</style>
</head>
<body>
  <section class="card card-front">
    <div class="brand">
      <span class="brand-dot"></span>
      <span class="brand-name">BRONSALK</span>
    </div>
    <div class="info-band">
      <div class="person">
        <p class="person-name">Paul Ardley</p>
        <p class="person-role">Director Operations</p>
      </div>
      <ul class="contacts">
        <li>+61 452 118 906
          <svg viewBox="0 0 10 10"><path d="M1 3.5C1 2 2.5 1 5 1s4 1 4 2.5L7.5 4.2 6.8 3H3.2L2.5 4.2zM2.5 9 3.4 4.5h3.2L7.5 9z"/></svg>
        </li>
        <li>paulardley@bronsalk.com
          <svg viewBox="0 0 10 10"><path d="M1 2h8v1L5 5.5 1 3zM1 4.2 5 6.7l4-2.5V8H1z"/></svg>
        </li>
        <li>www.bronsalk.com
          <svg viewBox="0 0 10 10"><circle cx="5" cy="5" r="4.5"/><path d="M3 3.2 5 2.6 5.6 4 4 5.4 4.6 7.2 3.2 6z" fill="#27a9e1"/></svg>
        </li>
      </ul>
    </div>
  </section>

  <section class="card card-back">
    <div class="type-texture" role="img" aria-label="Faint rotated typographic texture of the words create, inspire and tomorrow in dark grey on black"></div>
    <h2 class="motto">
      <span>CREATE</span>
      <span>INSPIRE</span>
      <span>TOMORROW</span>
    </h2>
  </section>
</body>
</html>
```